Buisness card

**Front Side:**

**[Your Company Logo]**
**Steadfast Upkeep Engineering**
*Keeping Your Equipment Running Smoothly*

**Contact Information:**
- **Name:** [dale Harwick
- **Title:** [owner
- **Phone:** [5073918246
- **Email:** dale@suevx.com

**Back Side:**

**Services Offered:**
- Routine Inspections
- Equipment Maintenance
- Emergency Repairs
- Consultation Services
- New installs
Tag line
Be proactive not reactive

```html
<!DOCTYPE html>
<html lang="en">
<head>
<meta charset="utf-8">
<title>Steadfast Upkeep Engineering — Business Card</title>
<link rel="stylesheet" href="https://fonts.googleapis.com/css2?family=Montserrat:wght@500;600;700&family=Arimo:wght@400;700&display=swap">
<style>
  :root {
    --bg: #a3b4c6;
    --paper: #ffffff;
    --navy: #263a86;
    --cyan: #35d8f5;
    --ink: #1a1a1a;
    --shadow: rgba(30, 45, 70, 0.28);
  }
  * { box-sizing: border-box; margin: 0; padding: 0; }
  html, body {
    width: 1200px; height: 988px; overflow: hidden;
    background: var(--bg);
  }
  .canvas {
    position: relative; width: 1200px; height: 988px;
    display: flex; flex-direction: column; align-items: center;
    justify-content: center; gap: 48px;
  }
  .card {
    position: relative; width: 700px; height: 400px;
    background: var(--paper);
    box-shadow: 0 14px 30px var(--shadow);
    overflow: hidden;
  }

  /* ---------- Back side ---------- */
  .back .brand-mark {
    position: absolute; left: 70px; top: 48px;
    display: flex; align-items: center; gap: 18px;
  }
  .brand-dot {
    width: 96px; height: 96px; border-radius: 50%;
    background: var(--navy); flex: none;
  }
  .brand-name {
    font-family: "Montserrat", sans-serif; font-weight: 700;
    color: var(--navy); font-size: 22px; line-height: 1.15;
    width: 200px;
  }
  .services {
    position: absolute; right: 70px; top: 150px;
    list-style: none;
    font-family: "Arimo", sans-serif; font-size: 23px;
    color: var(--navy); line-height: 1.32;
  }
  .services li { display: flex; align-items: center; gap: 14px; }
  .services li::before {
    content: ""; width: 10px; height: 10px; background: var(--cyan); flex: none;
  }
  .back .motto {
    position: absolute; left: 50px; bottom: 44px;
    font-family: "Montserrat", sans-serif; font-weight: 600;
    font-variant: small-caps; font-size: 44px; letter-spacing: 1px;
    color: var(--navy);
  }

  /* ---------- Front side ---------- */
  .front .header {
    position: absolute; left: 0; top: 0; width: 100%; height: 205px;
    display: flex; align-items: center; padding: 0 40px; gap: 26px;
  }
  .front .brand-dot { width: 118px; height: 118px; }
  .front .company {
    font-family: "Montserrat", sans-serif; font-weight: 700;
    color: var(--navy); font-size: 34px; line-height: 1.1;
  }
  .front .company-tag {
    margin-top: 10px;
    font-family: "Montserrat", sans-serif; font-weight: 700;
    color: var(--ink); font-size: 19px; letter-spacing: 0.5px;
  }
  .contact-band {
    position: absolute; left: 0; top: 205px; width: 100%; height: 125px;
    background: var(--navy); color: #fff;
    display: flex; justify-content: space-between; align-items: center;
    padding: 0 40px;
  }
  .person-name {
    font-family: "Montserrat", sans-serif; font-weight: 600;
    font-variant: small-caps; font-size: 40px; letter-spacing: 1px;
    text-transform: capitalize;
  }
  .person-title {
    font-family: "Arimo", sans-serif; font-size: 22px; margin-top: 2px;
  }
  .contact-list {
    list-style: none; font-family: "Arimo", sans-serif; font-size: 22px;
    line-height: 1.5;
  }
  .contact-list li { display: flex; align-items: center; gap: 12px; justify-content: flex-end; }
  .contact-list svg { width: 22px; height: 22px; fill: #fff; }
  .slogan-band {
    position: absolute; left: 0; bottom: 0; width: 100%; height: 70px;
    background: var(--cyan);
    display: flex; align-items: center; justify-content: center;
    font-family: "Montserrat", sans-serif; font-weight: 600;
    font-variant: small-caps; font-size: 26px; letter-spacing: 1.5px;
    color: var(--navy);
  }
</style>
</head>
<body>
<main class="canvas">

  <section class="card back" aria-label="Card back">
    <div class="brand-mark">
      <span class="brand-dot"></span>
      <span class="brand-name">Steadfast Upkeep Engineering</span>
    </div>
    <ul class="services">
      <li>Routine Inspections</li>
      <li>Equipment Maintenance</li>
      <li>Emergency Repairs</li>
      <li>Consultation Services</li>
      <li>New installs</li>
    </ul>
    <p class="motto">Be proactive Not reactive</p>
  </section>

  <section class="card front" aria-label="Card front">
    <header class="header">
      <span class="brand-dot"></span>
      <div>
        <p class="company">Steadfast Upkeep Engineering</p>
        <p class="company-tag">BE PROACTIVE NOT REACTIVE</p>
      </div>
    </header>
    <div class="contact-band">
      <div>
        <p class="person-name">dale Harwick</p>
        <p class="person-title">Owner</p>
      </div>
      <ul class="contact-list">
        <li>507 391 8246
          <svg viewBox="0 0 24 24" aria-hidden="true"><path d="M6.6 10.8a15.1 15.1 0 0 0 6.6 6.6l2.2-2.2a1 1 0 0 1 1-.25 11.4 11.4 0 0 0 3.6.57 1 1 0 0 1 1 1V20a1 1 0 0 1-1 1A17 17 0 0 1 3 4a1 1 0 0 1 1-1h3.5a1 1 0 0 1 1 1c0 1.25.2 2.45.57 3.57a1 1 0 0 1-.25 1z"/></svg>
        </li>
        <li>dale@suevx.com
          <svg viewBox="0 0 24 24" aria-hidden="true"><path d="M2 5h20v14H2zm2 2v.5l8 5 8-5V7l-8 5z"/></svg>
        </li>
      </ul>
    </div>
    <div class="slogan-band">Keeping Your Equipment Running Smoothly</div>
  </section>

</main>
</body>
</html>
```